Amber Hollow Business Card and Logo

Nutrition and Wellness Store Front. I sell supplements, herbs, tinctures, Loose Leaf Teas, natural snacks and drinks including gluten free. classes: Fitness; health and wellness; community health and wellness hub. It is a "shabby chic" store front. It is white and my accent color is turqouise I will be adding some jewelry, stones and rocks and jewelery. I am a Certified Herbalist and Certified Nutrition and Wellness Consultant, a Vosari Practitioner and Kaloro instructor.

Target Market(s)

health and wellness seekers, fitness, baby boomer

Industry/Entity Type

Business

Contact Information for Business Card

Amber Hollow Nutrition and Wellness
Linda Marcovitch Certified Herbalist , Certified Nutrition and Wellness Consultant, Vosari Practitioner, Kaloro Instructor

Font styles to use
Serif

Colors
33a6d7
3176b5
33b8a4

Requirements
Must have
• A picture that represents two mountain peaks with a floral accent.

```html
<!DOCTYPE html>
<html lang="en">
<head>
<meta charset="utf-8">
<title>Amber Hollow Nutrition and Wellness – Business Card</title>
<link href="https://fonts.googleapis.com/css2?family=Questrial&display=swap" rel="stylesheet">
<style>
  :root {
    --page-bg: #e9e6e1;
    --card-white: #ffffff;
    --accent-blue: #33a6d7;
    --deep-blue: #3176b5;
    --text-grey: #4a4a4a;
    --text-dark: #2b2b2b;
    --leaf-tint: #dfe8e1;
  }
  * { margin: 0; padding: 0; box-sizing: border-box; }
  html, body {
    width: 1200px;
    height: 848px;
    overflow: hidden;
    background: var(--page-bg);
    font-family: "Questrial", "Century Gothic", sans-serif;
  }
  .stage {
    width: 1200px;
    height: 848px;
    display: flex;
    align-items: center;
    justify-content: center;
  }
  .business-card {
    position: relative;
    width: 1050px;
    height: 600px;
    background: var(--card-white);
    box-shadow: 0 6px 24px rgba(0,0,0,0.15);
    overflow: hidden;
  }
  .leaf-accent {
    position: absolute;
    left: 700px;
    top: 120px;
    width: 300px;
    height: 420px;
    border-radius: 50% 40% 45% 50%;
    background: radial-gradient(ellipse at center, var(--leaf-tint) 0%, rgba(223,232,225,0.4) 55%, rgba(255,255,255,0) 75%);
  }
  .brand-name {
    position: absolute;
    left: 60px;
    top: 175px;
    color: var(--accent-blue);
    font-size: 46px;
    line-height: 1.05;
  }
  .contact-block {
    position: absolute;
    left: 660px;
    top: 48px;
    font-size: 27px;
    line-height: 1.3;
    color: var(--text-dark);
  }
  .contact-block .person-name { color: var(--text-grey); }
  .contact-block .phone {
    color: var(--accent-blue);
    letter-spacing: 6px;
  }
  .credentials {
    position: absolute;
    right: 70px;
    top: 300px;
    text-align: center;
    font-size: 26px;
    line-height: 1.3;
    color: var(--text-dark);
  }
  .web-band {
    position: absolute;
    left: 0;
    top: 395px;
    width: 100%;
    height: 125px;
    background: var(--accent-blue);
    display: flex;
    align-items: center;
    padding-left: 60px;
  }
  .web-address {
    color: var(--card-white);
    font-size: 38px;
    letter-spacing: 9px;
  }
</style>
</head>
<body>
  <main class="stage">
    <article class="business-card">
      <div class="leaf-accent" role="img" aria-label="Faint decorative leaf and vine accent"></div>

      <h1 class="brand-name">Amber Hollow<br>Nutrition and Wellness</h1>

      <address class="contact-block" style="font-style: normal;">
        <div class="person-name">Linda Marcovitch</div>
        <div class="phone">360-555-0147</div>
        <div>48 Cedar Hollow Lane</div>
        <div>Maple Falls, Oregon</div>
      </address>

      <p class="credentials">
        Certified Herbalist | Certified Nutrition and Wellness Consultant<br>
        Vosari Practitioner | Kaloro instructor
      </p>

      <div class="web-band">
        <span class="web-address">www.amberhollowwellness.com</span>
      </div>
    </article>
  </main>
</body>
</html>
```